■書籍タイトル
「町工房・路地の店・士業のための、明日効く集客設計術・KRT」

・堅苦しくなく、わかりやすいイメージにしたいです
・電子書籍なので、画像が小さいので、できるだけ視認しやすい文字でお願いします

■オビ
「お金も時間もかけずに、たった2つのことをするだけで、ライバルが歯ぎしりするほどお客に選ばれる」

■著者  森野沙知絵
■発行  東陽商務文化出版舎

■色の指定などはありません。お任せです。
(明るい・カンタン・わかりやすい)
イメージイラストなど入ってもよいかと思います。

■高級感やアカデミックより、明るくカンタンなイメージで。

※参考資料として、書籍の原稿と、同じタイトルのセミナーのパワポ表紙画像を添付します。
アカデミックな感じより、ポップな感じや明るいイメージ、
「わかりやすさ」「文字の視認性」を重視します。
クラフターのみなさま、
引き続き、ご提案をお待ちしております。
みなさま、ご提案ありがとうございます。

町工房・路地の店・士業
という文字が小さい表示のデザインが多いのですが、

ターゲット層が一目で見てわかるよう、

町工房・路地の店・士業

という文字が見えるようにしたいです。

引き続き、みなさまからのご提案をお待ちしております。
たくさんのご提案をいただきありがとうございます。

本のタイトルが、変更となりました。
金額をアップし、締め切りを1日延長いたしますので、
訂正ご対応いただければ幸いです。

新しいタイトルは、

「町工房・路地の店・士業が
常連が増え続けるために明日から始める三つの習慣」
です。

帯、またはサブタイトルは、
「ライバルが歯ぎしりするほどお客が押し寄せる明日効く集客設計術」
としてください。

ご提案をお待ちしております。
よろしくお願いいたします。

今回の装丁は、特に「わかりやすさ」を重視しておりました。
レベルの高い装丁デザインが多く、選考に大変迷いました。
選定させていただきましたデザインは、笑顔の3職種の人物のイラストと、フォントの使い方など、わかりやすい・明るい・カンタンという目指すところをこちらの想定以上に表現していただいたことが一番の理由です。

たくさんのご提案をいただき、ありがとうございました。
本当にレベルの高いデザインが多く選定では社内でも意見が割れました。
また、再三の追記・変更によりお手数をおかけしましたことを、この場を借りてお詫び申し上げます。

今後も定期的に装丁の依頼をいたしますので、どうぞよろしくお願いいたします。

```html
<!DOCTYPE html>
<html lang="ja">
<head>
<meta charset="utf-8">
<title>町工房・路地の店・士業が 常連が増え続けるために明日から始める三つの習慣</title>
<link rel="stylesheet" href="https://fonts.googleapis.com/css2?family=Noto+Sans+JP:wght@700;900&display=swap">
<style>
  :root {
    --blue-top: #3a86d6;
    --blue-bottom: #1c5fae;
    --white: #ffffff;
    --ink: #111111;
    --red: #e50012;
    --art-a: #f3e9d6;
    --art-b: #dfeaf5;
  }
  * { margin: 0; padding: 0; box-sizing: border-box; }
  html, body { width: 750px; height: 1200px; overflow: hidden; background: var(--white); }
  .cover {
    position: relative; width: 750px; height: 1200px; overflow: hidden;
    background: var(--white);
    font-family: "Noto Sans JP", sans-serif; font-weight: 900; color: var(--ink);
  }
  .title-field {
    position: absolute; left: 0; top: 0; width: 750px; height: 492px;
    background: linear-gradient(180deg, var(--blue-top), var(--blue-bottom));
  }
  .audience {
    position: absolute; top: 26px; left: 0; width: 100%;
    text-align: center; color: var(--white); font-size: 38px; font-weight: 700; letter-spacing: 1px;
  }
  .title-box { position: absolute; left: 14px; width: 722px; background: var(--white); }
  .title-box--first { top: 80px; height: 150px; }
  .title-box--second { top: 252px; height: 90px; }
  .title-box--third { top: 364px; height: 104px; }
  .title-main {
    position: absolute; left: 30px; top: 6px; font-size: 72px; line-height: 1.2; letter-spacing: -1px;
  }
  .title-main .particle { font-size: 52px; }
  .title-tail { position: absolute; right: 30px; top: 94px; font-size: 44px; line-height: 1.1; }
  .title-action { width: 100%; text-align: center; font-size: 76px; line-height: 90px; letter-spacing: 2px; }
  .title-count { width: 100%; text-align: center; font-size: 60px; line-height: 104px; letter-spacing: 2px; }
  .title-count .num { font-size: 92px; }
  .accent { color: var(--red); }
  .illustration {
    position: absolute; left: 40px; top: 580px; width: 380px; height: 460px;
    border-radius: 24px;
    background: radial-gradient(ellipse at 45% 45%, var(--art-a), var(--art-b) 80%, var(--white));
  }
  .tagline {
    position: absolute; right: 16px; top: 596px;
    display: flex; flex-direction: row-reverse; gap: 8px;
  }
  .tagline .col {
    writing-mode: vertical-rl; font-size: 46px; line-height: 1;
  }
  .tagline .indent { padding-top: 50px; }
  .tagline .sub { font-size: 44px; color: var(--red); }
  .tagline .sub-first { margin-right: 10px; }
  .credits {
    position: absolute; left: 470px; top: 1076px;
    font-size: 20px; font-weight: 700; line-height: 34px; color: var(--ink); white-space: nowrap;
  }
</style>
</head>
<body>
<div class="cover">
  <div class="title-field">
    <p class="audience">町工房・路地の店・士業が</p>
    <div class="title-box title-box--first">
      <p class="title-main">常連<span class="particle">が</span>増え続ける</p>
      <p class="title-tail">ために</p>
    </div>
    <div class="title-box title-box--second">
      <p class="title-action"><span class="accent">明日から</span>始める</p>
    </div>
    <div class="title-box title-box--third">
      <p class="title-count">たった<span class="accent num">三</span>つの習慣</p>
    </div>
  </div>

  <div class="illustration" role="img" aria-label="笑顔の職人・店主・士業の三職種の人物が線でつながるイラスト"></div>

  <div class="tagline">
    <span class="col">「<span class="accent">ライバル</span>が</span>
    <span class="col indent">歯ぎしりするほど</span>
    <span class="col indent">お客が<span class="accent">押し寄せる</span></span>
    <span class="col sub sub-first">明日効く</span>
    <span class="col sub indent">集客設計術」</span>
  </div>

  <div class="credits">
    <p>■著者　森野沙知絵</p>
    <p>■発行　東陽商務文化出版舎</p>
  </div>
</div>
</body>
</html>
```